Velmora Partners - website for real estate investment company

Create a bold, modern website that reflects Velmora’s success, professionalism, and credibility.
The design must stand out while maintaining a polished, corporate tone. (bold, but understated)
The client just created a new logo, and the website design must be in sync with the logo design. Information about the logo colors, fonts, and message are in the attached design brief.
Updates

Target Market(s)

b2b: banks, brokers, institutional partners, vendors, and property sellers.

Industry/Entity Type

real estate investment company

Number of Pages Required

1 page

Font styles to use
Sans Serif

Colors

Designer to choose colors to be used in the design.

Requirements
Must have
• 1. homepage design (psd) 2. a top banner image (psd) for a default inner page
Nice to have
• please see attached design brief
Should not have

```html
<!DOCTYPE html>
<html lang="en">
<head>
<meta charset="utf-8">
<title>Velmora Partners</title>
<link href="https://fonts.googleapis.com/css2?family=Barlow:wght@400;500;600;700&family=Barlow+Semi+Condensed:wght@500;600;700;800&display=swap" rel="stylesheet">
<style>
:root{
  --red:#d71f26;
  --ink:#1a1a1a;
  --body:#333;
  --grey-btn:#4a4a4a;
  --light:#f0f0f0;
  --black:#0b0b0b;
  --line:#d6d6d6;
}
*{margin:0;padding:0;box-sizing:border-box}
html,body{width:1200px;height:3168px;overflow:hidden;background:#fff}
body{position:relative;font-family:"Barlow",Arial,sans-serif;color:var(--body)}
.abs{position:absolute}
.heading{font-family:"Barlow Semi Condensed","Arial Narrow",sans-serif;font-weight:700;color:var(--red);text-transform:uppercase;letter-spacing:.5px}
.btn{position:absolute;display:flex;align-items:center;justify-content:center;font-size:10px;font-weight:600;color:#fff;letter-spacing:.5px;text-transform:uppercase;background:var(--grey-btn)}
.btn.red{background:var(--red)}

/* header */
.site-header{position:absolute;left:0;top:0;width:1200px;height:62px;background:#fff;border-bottom:1px solid #ddd}
.brand{position:absolute;left:150px;top:12px;font-family:"Barlow Semi Condensed",sans-serif;font-weight:700;font-size:34px;color:#3a3a3a;letter-spacing:1px}
.main-nav{position:absolute;left:388px;top:25px;display:flex;gap:19px;font-size:11px;font-weight:500;color:#333;text-transform:uppercase}
.main-nav .active{color:var(--red)}
.head-icon{position:absolute;top:15px;width:31px;height:31px;border:1px solid #666;display:flex;align-items:center;justify-content:center}

/* hero */
.hero{position:absolute;left:0;top:62px;width:1200px;height:470px;background:linear-gradient(180deg,#3b3c42 0%,#2a2d35 45%,#1f2229 100%)}
.hero-title{position:absolute;top:176px;left:0;width:1200px;text-align:center;font-size:34px;font-weight:800}
.hero-text{position:absolute;top:226px;left:300px;width:600px;text-align:center;font-size:14.5px;line-height:18px;color:#fff}

/* stats */
.stats{position:absolute;left:0;top:532px;width:1200px;height:152px;background:var(--black)}
.stat{position:absolute;top:50px;display:flex;align-items:center;gap:12px;color:#fff}
.stat-icon{width:56px;height:56px;background:#1d1d1d;display:flex;align-items:center;justify-content:center;clip-path:polygon(20% 0,100% 0,80% 100%,0 100%)}
.stat b{display:block;font-family:"Barlow Semi Condensed",sans-serif;font-size:30px;font-weight:700;line-height:30px}
.stat span{font-size:16px;font-weight:500}

/* split sections */
.frame-red{position:absolute;background:var(--red)}
.photo{position:absolute}
.badge{position:absolute;left:493px;top:872px;width:113px;height:209px;background:#fff;border-right:4px solid var(--red);box-shadow:0 2px 8px rgba(0,0,0,.15)}
.badge-text{position:absolute;left:50%;top:50%;transform:translate(-50%,-50%) rotate(-90deg);white-space:nowrap;font-family:"Barlow Semi Condensed",sans-serif;font-size:30px;line-height:32px}
.badge-text .y{color:var(--red);font-weight:800}
.badge-text .e{color:#777;font-weight:500;font-size:27px}
.sec-title{font-size:27px}
.lead{font-size:13px;font-weight:600;color:#111;line-height:16px}
.copy{font-size:12px;line-height:16px;color:#333}
.strategy-bg{position:absolute;left:0;top:1200px;width:617px;height:366px;background:var(--light)}
.bullets{position:absolute;left:150px;top:1316px;list-style:none;font-size:12.5px;color:#333}
.bullets li{height:21.3px;display:flex;align-items:center;gap:6px}
.bullets li::before{content:"";width:11px;height:11px;border-radius:50%;background:#8a8a8a}

/* portfolio */
.portfolio{position:absolute;left:0;top:2037px;width:1200px;height:493px;background:var(--black)}
.portfolio-title{position:absolute;top:66px;width:1200px;text-align:center;color:#fff;font-family:"Barlow Semi Condensed",sans-serif;font-size:28px;font-weight:700}
.tile{position:absolute;top:122px;width:398px;height:371px}
.tile-label{position:absolute;left:12px;right:12px;bottom:10px;height:48px;background:rgba(20,20,20,.7);color:#fff;font-size:19px;font-weight:500;display:flex;align-items:center;justify-content:center;text-transform:uppercase}
.tile-label.on{background:var(--red)}

/* inquiry */
.field-label{position:absolute;font-size:11px;color:#333}
.field{position:absolute;height:31px;border:1px solid var(--line);background:#fff}
.field svg{position:absolute;left:10px;top:9px}

/* footer */
.site-footer{position:absolute;left:0;top:2920px;width:1200px;height:215px;background:linear-gradient(180deg,#1b1c20,#121316)}
.foot-brand{position:absolute;left:150px;top:46px;font-family:"Barlow Semi Condensed",sans-serif;font-weight:700;font-size:38px;color:#fff;letter-spacing:1px}
.foot-head{position:absolute;top:56px;font-size:16px}
.foot-list{position:absolute;list-style:none;font-size:11px;color:#fff}
.foot-list li{height:19px;display:flex;align-items:center;gap:10px}
.foot-links{position:absolute;list-style:none;font-size:11px;color:#fff}
.foot-links li{height:19px}
.map{position:absolute;left:856px;top:58px;width:195px;height:103px;background:linear-gradient(135deg,#eef1f5,#dde4ec)}
.copybar{position:absolute;left:0;top:3135px;width:1200px;height:33px;background:var(--red);color:#fff;font-size:11px}
.social{position:absolute;top:9px;width:15px;height:15px;border-radius:50%;border:1.5px solid #fff}
</style>
</head>
<body>

<header class="site-header">
  <div class="brand">VELMORA</div>
  <nav class="main-nav">
    <span class="active">Home</span><span>Our Story</span><span>Investment Strategy</span><span>What Sets Us Apart</span><span>Our Portfolio</span><span>Contact Us</span>
  </nav>
  <div class="head-icon" style="left:981px"><svg width="12" height="9" viewBox="0 0 12 9"><rect width="12" height="9" fill="#d71f26"/><path d="M0 0l6 5 6-5" stroke="#fff" fill="none"/></svg></div>
  <div class="head-icon" style="left:1019px"><svg width="12" height="12" viewBox="0 0 24 24"><path d="M6 2l4 5-2 3c1 2 4 5 6 6l3-2 5 4-3 4C10 21 3 14 2 5z" fill="#d71f26"/></svg></div>
</header>

<section class="hero" role="img" aria-label="Aerial view of a city skyline with glass towers at dusk">
  <h1 class="hero-title heading">Experience – Strategy – Vision</h1>
  <p class="hero-text">Velmora Partners is a vertically integrated real estate investment firm with a proven four-decade track record. We acquire, reposition, and operate high-performing assets across multiple sectors - always with a focus on exceptional, risk-adjusted returns.</p>
</section>

<section class="stats">
  <div class="stat" style="left:168px">
    <div class="stat-icon"><svg width="30" height="32" viewBox="0 0 30 32" fill="none" stroke="#d71f26" stroke-width="2"><circle cx="15" cy="9" r="6"/><path d="M3 31c0-8 5-12 12-12s12 4 12 12z"/></svg></div>
    <div><b>1989</b><span>Founded</span></div>
  </div>
  <div class="stat" style="left:368px">
    <div class="stat-icon"><svg width="34" height="32" viewBox="0 0 34 32" fill="none" stroke="#d71f26" stroke-width="2"><rect x="10" y="4" width="14" height="27"/><rect x="2" y="14" width="8" height="17"/><rect x="24" y="14" width="8" height="17"/><path d="M17 8v6M14 11h6"/></svg></div>
    <div><b>23,000+</b><span>Multifamily &amp; healthcare units</span></div>
  </div>
  <div class="stat" style="left:728px">
    <div class="stat-icon"><svg width="36" height="32" viewBox="0 0 36 32" fill="none" stroke="#d71f26" stroke-width="2"><circle cx="18" cy="8" r="6" fill="#fff" stroke="none"/><path d="M2 24l10-6h8l-2 4h-6M16 22l14-6 4 2-16 12H4"/></svg></div>
    <div><b>$300+</b><span>Million invested in renovations</span></div>
  </div>
</section>

<section>
  <div class="frame-red" style="left:150px;top:753px;width:136px;height:127px;clip-path:polygon(0 0,100% 0,0 100%)"></div>
  <div class="frame-red" style="left:442px;top:996px;width:136px;height:128px;clip-path:polygon(100% 0,100% 100%,0 100%)"></div>
  <div class="photo" style="left:162px;top:766px;width:404px;height:345px;background:linear-gradient(135deg,#2b2b2e,#c9b39a 55%,#e4e2de)" role="img" aria-label="Business team joining hands over a table"></div>
  <div class="badge"><div class="badge-text"><span class="y">40 YEARS</span><br><span class="e">OF EXPERIENCE</span></div></div>
  <h2 class="abs heading sec-title" style="left:682px;top:828px">Our Story</h2>
  <p class="abs lead" style="left:682px;top:877px;width:360px">Velmora Partners is a real estate investment company</p>
  <p class="abs copy" style="left:682px;top:894px;width:360px">that has been successfully buying, improving, and managing properties for over 40 years.</p>
  <p class="abs copy" style="left:682px;top:943px;width:360px">We focus on making smart investments in different types of real estate to deliver strong, reliable returns while carefully managing risk.</p>
  <div class="btn" style="left:682px;top:1013px;width:92px;height:30px">Read More</div>
</section>

<section>
  <div class="strategy-bg"></div>
  <h2 class="abs heading sec-title" style="left:150px;top:1267px">Investment Strategy</h2>
  <ul class="bullets">
    <li>Lorem ipsum dolor sit amet, consectetur adipiscing elit.</li>
    <li>Aliquam vitae velit ac metus luctus convallis.</li>
    <li>Nunc sit amet est nec erat tincidunt tempor et sed nisi.</li>
    <li>Duis facilisis eros eget fermentum aliquet.</li>
    <li>Donec a erat id nunc malesuada suscipit.</li>
    <li>Integer porttitor lorem a justo laoreet sollicitudin.</li>
  </ul>
  <div class="btn red" style="left:150px;top:1460px;width:92px;height:29px">Read More</div>
  <div class="photo" style="left:617px;top:1200px;width:583px;height:366px;background:linear-gradient(135deg,#0f1f3d,#1e3c6e 50%,#0a1426)" role="img" aria-label="Hand above a glowing 3D bar chart on a world map"></div>
</section>

<section>
  <div class="frame-red" style="left:150px;top:1622px;width:136px;height:127px;clip-path:polygon(0 0,100% 0,0 100%)"></div>
  <div class="frame-red" style="left:442px;top:1834px;width:136px;height:127px;clip-path:polygon(100% 0,100% 100%,0 100%)"></div>
  <div class="photo" style="left:162px;top:1634px;width:404px;height:315px;background:linear-gradient(180deg,#5b9ad8 0%,#9cc4e8 40%,#6f7c88 75%,#6c8a4c)" role="img" aria-label="Modern glass apartment building under a blue sky"></div>
  <h2 class="abs heading sec-title" style="left:653px;top:1685px">What Sets Us Apart</h2>
  <p class="abs lead" style="left:653px;top:1733px;width:360px">Lorem Ipsum is simply dummy text of the printing and typesetting industry.</p>
  <p class="abs copy" style="left:653px;top:1783px;width:360px">Lorem Ipsum has been the industry's standard dummy text ever since the 1500s, when an unknown printer took a galley of type and scrambled it to make a type specimen book. It has survived not only five centuries, but also the leap into electronic typesetting, remaining essentially unchanged.</p>
  <div class="btn" style="left:653px;top:1886px;width:92px;height:30px">Read More</div>
</section>

<section class="portfolio">
  <h2 class="portfolio-title">OUR PORTFOLIO</h2>
  <div class="tile" style="left:0;background:linear-gradient(180deg,#8fa3b8,#2c4a6a 55%,#14243a)" role="img" aria-label="Glass office tower at sunset"><div class="tile-label">Office</div></div>
  <div class="tile" style="left:401px;background:linear-gradient(180deg,#b8b6a8,#8a8b7e 40%,#5f7d3a)" role="img" aria-label="Aerial view of a white multifamily building on a lawn"><div class="tile-label">Multifamily</div></div>
  <div class="tile" style="left:802px;background:linear-gradient(135deg,#4a3e34,#9a8a74 50%,#3a3a46)" role="img" aria-label="Clothing store interior with racks of shirts"><div class="tile-label on">Retail</div></div>
</section>

<section>
  <h2 class="abs heading" style="left:0;top:2595px;width:1200px;text-align:center;font-size:29px">Quick Inquiry</h2>
  <label class="field-label" style="left:290px;top:2654px">Name</label>
  <label class="field-label" style="left:503px;top:2654px">Your Email</label>
  <label class="field-label" style="left:715px;top:2654px">Phone Number</label>
  <div class="field" style="left:290px;top:2672px;width:195px"><svg width="10" height="11" viewBox="0 0 10 11" fill="none" stroke="#d71f26"><circle cx="5" cy="3" r="2.5"/><path d="M.5 10.5c0-3 2-4.5 4.5-4.5s4.5 1.5 4.5 4.5z"/></svg></div>
  <div class="field" style="left:503px;top:2672px;width:194px"><svg width="11" height="9" viewBox="0 0 11 9" fill="none" stroke="#d71f26"><rect x=".5" y=".5" width="10" height="8"/><path d="M.5.5l5 4 5-4"/></svg></div>
  <div class="field" style="left:715px;top:2672px;width:195px"><svg width="8" height="12" viewBox="0 0 8 12" fill="none" stroke="#d71f26"><rect x=".5" y=".5" width="7" height="11" rx="1"/></svg></div>
  <label class="field-label" style="left:290px;top:2716px">Your Message</label>
  <div class="field" style="left:290px;top:2735px;width:620px;height:72px"><svg width="10" height="10" viewBox="0 0 10 10" fill="none" stroke="#d71f26"><path d="M.5.5h9v6l-3 3h-6z"/></svg></div>
  <div class="btn" style="left:561px;top:2839px;width:78px;height:30px">Submit</div>
</section>

<footer class="site-footer">
  <div class="foot-brand">VELMORA</div>
  <h3 class="heading foot-head" style="left:351px">Contact Info</h3>
  <ul class="foot-list" style="left:351px;top:85px">
    <li style="height:28px"><svg width="11" height="14" viewBox="0 0 11 14"><path d="M5.5 0A5.5 5.5 0 0 0 0 5.5C0 9 5.5 14 5.5 14S11 9 11 5.5A5.5 5.5 0 0 0 5.5 0z" fill="#d71f26"/><circle cx="5.5" cy="5.5" r="2" fill="#1b1c20"/></svg>2240 Harbor Rd, Lakeview, NJ 08100</li>
    <li style="height:28px"><svg width="11" height="11" viewBox="0 0 24 24"><path d="M6 2l4 5-2 3c1 2 4 5 6 6l3-2 5 4-3 4C10 21 3 14 2 5z" fill="#d71f26"/></svg>(555) 014-2290</li>
    <li style="height:22px"><svg width="12" height="9" viewBox="0 0 12 9"><rect width="12" height="9" fill="#d71f26"/><path d="M0 0l6 5 6-5" stroke="#1b1c20" fill="none"/></svg>info@velmora.com</li>
  </ul>
  <h3 class="heading foot-head" style="left:573px">Quick Link</h3>
  <ul class="foot-links" style="left:573px;top:88px"><li style="color:var(--red)">Home</li><li>Our Story</li><li>Investment Strategy</li><li>What Sets Us Apart</li></ul>
  <ul class="foot-links" style="left:702px;top:88px"><li>Our Portfolio</li><li>Contact Us</li><li>Trams &amp; Condition</li><li>Privacy Policy</li></ul>
  <div class="map" role="img" aria-label="Street map showing the office location"></div>
</footer>

<div class="copybar">
  <span class="abs" style="left:150px;top:10px">© 2025 VELMORA. All Right Reserved</span>
  <span class="social" style="left:928px"></span>
  <span class="social" style="left:953px;background:#fff;width:20px;height:20px;top:6px"></span>
  <span class="social" style="left:984px"></span>
  <span class="social" style="left:1011px"></span>
  <span class="social" style="left:1038px"></span>
</div>

</body>
</html>
```